Property investment company needs a letterhead design!

We are a new residential and commercial property investment company. Name of the company is Morvesta Group, LLC. We have a new logo and now we need letterhead! We prefer to have a professional and upscale appearance. We don't have any fixed requirements, so be creative! Thank you for considering this project. We are so excited to see what happens!

Target Market(s)

Professional

Industry/Entity Type

Real Estate Development

```html
<!DOCTYPE html>
<html lang="en">
<head>
<meta charset="utf-8">
<title>Morvesta Group, LLC — Letterhead</title>
<link href="https://fonts.googleapis.com/css2?family=Open+Sans:wght@400;600;700&family=Raleway:wght@300;400&family=Great+Vibes&display=swap" rel="stylesheet">
<style>
  :root {
    --navy: #21324b;
    --sky: #00a0e6;
    --ink: #333a44;
    --paper: #ffffff;
    --canvas: #ffffff;
  }
  * { box-sizing: border-box; margin: 0; padding: 0; }
  html, body { width: 1200px; height: 1200px; overflow: hidden; background: var(--canvas); }
  body { font-family: "Open Sans", Arial, sans-serif; color: var(--ink); }

  .letterhead {
    position: absolute; left: 219px; top: 59px;
    width: 770px; height: 1089px;
    background: var(--paper);
    box-shadow: 0 0 14px rgba(0,0,0,0.12);
    overflow: hidden;
  }
  .frame-art { position: absolute; inset: 0; width: 770px; height: 1089px; }

  .brand {
    position: absolute; left: 100px; top: 112px;
    display: flex; align-items: center; gap: 8px;
  }
  .brand-dot { width: 14px; height: 14px; border-radius: 50%; background: var(--sky); flex: none; }
  .brand-name {
    font-weight: 700; font-size: 17px; line-height: 1.15; color: var(--navy);
    letter-spacing: 0.5px; text-transform: uppercase;
  }

  .sender { position: absolute; left: 100px; top: 218px; }
  .sender-name { color: var(--sky); font-size: 12.6px; line-height: 19px; }
  .sender-role { font-size: 9.6px; line-height: 16px; margin-bottom: 3px; }
  .contact-row { font-size: 11.8px; line-height: 19px; display: flex; }
  .contact-key { width: 24px; font-weight: 700; color: var(--sky); }
  .contact-key.dark { color: var(--ink); }

  .date { position: absolute; right: 100px; top: 296px; font-size: 11.8px; line-height: 19px; }

  .body-copy { position: absolute; left: 100px; top: 357px; width: 600px; }
  .paragraph { margin-bottom: 24.4px; }
  .line { display: block; font-size: 12.2px; line-height: 24.8px; white-space: nowrap; }

  .sign-off { position: absolute; left: 100px; top: 768px; }
  .signature { font-family: "Great Vibes", cursive; font-size: 28px; line-height: 34px; color: var(--navy); }
  .signer-name { font-weight: 700; font-size: 12.4px; line-height: 14px; margin-top: 0; }
  .signer-role { font-size: 12px; line-height: 14px; }

  .footer-contacts {
    position: absolute; right: 22px; top: 1043px;
    display: flex; align-items: center; gap: 10px;
    font-family: "Raleway", Arial, sans-serif; font-weight: 400;
    color: #fff; font-size: 10.2px; line-height: 13px;
  }
  .footer-item { display: flex; align-items: center; gap: 12px; }
  .footer-item .text { text-align: right; }
  .footer-icon { width: 16px; height: 18px; flex: none; }
  .footer-icon.wide { width: 26px; height: 20px; }
</style>
</head>
<body>
<main class="letterhead">
  <svg class="frame-art" viewBox="0 0 1232 1742" aria-hidden="true">
    <!-- header bands -->
    <polygon fill="var(--navy)" points="0,0 963,0 1232,269 1232,402 925,95 0,95"/>
    <polygon fill="var(--sky)" stroke="#fff" stroke-width="16" stroke-linejoin="miter"
      points="-20,111 1141,111 1240,210 1240,253 1128,142 -20,142"/>
    <line x1="1070" y1="263" x2="1150" y2="330" stroke="var(--sky)" stroke-width="1"/>
    <!-- footer bands -->
    <polygon fill="var(--navy)" points="0,1340 307,1647 1232,1647 1232,1742 270,1742 0,1473"/>
    <polygon fill="var(--sky)" stroke="#fff" stroke-width="16" stroke-linejoin="miter"
      points="-10,1487 103,1600 1250,1600 1250,1631 90,1631 -10,1533"/>
  </svg>

  <div class="brand">
    <span class="brand-dot"></span>
    <div class="brand-name">Morvesta<br>Group, LLC</div>
  </div>

  <section class="sender">
    <p class="sender-name">Elena Harwick</p>
    <p class="sender-role">Chief Director</p>
    <p class="contact-row"><span class="contact-key">A :</span>12-4, Calder Quay Singapore - 4170</p>
    <p class="contact-row"><span class="contact-key dark">W :</span>hello@morvesta.com, www.morvesta.com</p>
    <p class="contact-row"><span class="contact-key">P :</span>+65 - 4821 - 3390</p>
  </section>

  <p class="date">Date, 10 September, 2019</p>

  <article class="body-copy">
    <p class="paragraph">
      <span class="line">This is a sample letter that has been placed to demonstrate typing remat (Your Company). letterhead</span>
      <span class="line">design. When positioned properly, it will serve to work in harmony with all other elements letterhead.</span>
      <span class="line">This letterhead design is meant to project an image</span>
    </p>
    <p class="paragraph">
      <span class="line">This letterhead design is meant project an image of professionalism reliability. By using simple aligen</span>
      <span class="line">we have created a very spacious feeling. The simplicity suggest&nbsp; rengththe spaciousnes contributes h</span>
      <span class="line">aesthetics the layout. These basic qualities along with the (Your Company)</span>
    </p>
    <p class="paragraph">
      <span class="line">look and helps reinforce the (Your Company) brand. letterhead design is meant to project an image p</span>
      <span class="line">design. When positioned properly, it will serve to work in harmony all the other elements letterhead.</span>
      <span class="line">sionalism and reliability.</span>
    </p>
    <p class="paragraph">
      <span class="line">This letterhead design is based on the (Form of your logo) form (Your Company) logo. Each stationery</span>
      <span class="line">we have created a very spacious feeling. The simplicity suggests strength the spaciousnes contribute</span>
      <span class="line">part of the (Form of your logo).</span>
    </p>
  </article>

  <section class="sign-off">
    <p class="signature">Daniel Ostrow</p>
    <p class="signer-name">Daniel Ostrow</p>
    <p class="signer-role">Manager</p>
  </section>

  <footer class="footer-contacts">
    <div class="footer-item">
      <div class="text">Street Address Here<br>Singapore, 2222</div>
      <svg class="footer-icon" viewBox="0 0 16 20"><path fill="#fff" d="M8 0a6.5 6.5 0 0 0-6.5 6.5C1.5 11.5 8 20 8 20s6.5-8.5 6.5-13.5A6.5 6.5 0 0 0 8 0zm0 9a2.5 2.5 0 1 1 0-5 2.5 2.5 0 0 1 0 5z"/></svg>
    </div>
    <div class="footer-item">
      <div class="text">urwebsitename.com<br>urname@email.com</div>
      <svg class="footer-icon" viewBox="0 0 20 20"><g fill="none" stroke="#fff" stroke-width="1.6"><circle cx="10" cy="10" r="8.2"/><path d="M3 6c4 1 6 4 5 8M17 6c-4 0-6 2-9 8M10 2c2 3 3 6 2 10"/></g></svg>
    </div>
    <div class="footer-item">
      <div class="text">+000 12345 6789<br>+000 12345 6789</div>
      <svg class="footer-icon wide" viewBox="0 0 26 20"><g fill="#fff"><path d="M1 6c0-3 6-5 12-5s12 2 12 5v2h-6V5.5c-2-.7-4-1-6-1s-4 .3-6 1V8H1z"/><path d="M7 8h12l4 6v5H3v-5z"/></g><g fill="var(--navy)"><rect x="10" y="11" width="1.6" height="1.6"/><rect x="12.2" y="11" width="1.6" height="1.6"/><rect x="14.4" y="11" width="1.6" height="1.6"/><rect x="10" y="13.4" width="1.6" height="1.6"/><rect x="12.2" y="13.4" width="1.6" height="1.6"/><rect x="14.4" y="13.4" width="1.6" height="1.6"/></g></svg>
    </div>
  </footer>
</main>
</body>
</html>
```